Halvern Stationary Design

We're seeking a fresh and modern design for our stationery that captures the essence of our Real Estate brand. The current design, while functional, lacks visual appeal. We're looking for a more attractive and engaging design that showcases our professionalism and expertise in the real estate industry. I am attaching the current letter head and an image with a letter "P" as logo.

Target Market(s)

Real Estate Sales and Rentals

Industry/Entity Type

Real Estate

Requirements
Nice to have
• The owner seems to like the letter "P"

```html
<!DOCTYPE html>
<html lang="en">
<head>
<meta charset="utf-8">
<title>Halvern Property Solutions – Stationery</title>
<link href="https://fonts.googleapis.com/css2?family=Didact+Gothic&family=Montserrat:wght@500;600;700&display=swap" rel="stylesheet">
<style>
  :root {
    --canvas: #ffffff;
    --paper: #f5f5f5;
    --paper-edge: #e3e3e3;
    --ink: #2b2b2b;
    --ink-soft: #3a3a3a;
    --dot: #9a9a9a;
    --flap-line: #bdbdbd;
  }
  * { margin: 0; padding: 0; box-sizing: border-box; }
  html, body { width: 1200px; height: 1200px; overflow: hidden; background: var(--canvas); }
  body { position: relative; font-family: "Didact Gothic", sans-serif; color: var(--ink); }

  .sheet, .card, .envelope {
    position: absolute;
    background: var(--paper);
    border: 1px solid var(--paper-edge);
  }

  /* brand name: one line, one weight, one colour, plain dot beside */
  .brand {
    position: absolute;
    left: 0; width: 100%;
    display: flex; align-items: center; justify-content: center;
    font-family: "Montserrat", sans-serif;
    font-weight: 600;
    color: var(--ink);
    white-space: nowrap;
  }
  .brand-dot { flex: none; border-radius: 50%; background: var(--dot); }

  /* cover sheet */
  .cover { left: 96px; top: 191px; width: 466px; height: 600px; }
  .cover .brand { top: 318px; font-size: 17px; gap: 10px; }
  .cover .brand-dot { width: 16px; height: 16px; }
  .cover-taglines {
    position: absolute; left: 0; width: 100%; top: 531px;
    text-align: center; font-size: 12px; line-height: 15.5px; color: var(--ink-soft);
  }

  /* letterhead */
  .letterhead { left: 646px; top: 191px; width: 466px; height: 600px; }
  .letterhead .brand { top: 88px; font-size: 12px; gap: 7px; }
  .letterhead .brand-dot { width: 11px; height: 11px; }
  .letterhead-rule { position: absolute; left: 53px; width: 361px; top: 117px; border-top: 1px solid var(--ink-soft); }

  .letter { position: absolute; left: 57px; width: 352px; top: 134px; font-size: 11px; line-height: 13.1px; }
  .person { font-family: "Montserrat", sans-serif; font-weight: 600; font-size: 14.5px; line-height: 17px; }
  .role { font-family: "Montserrat", sans-serif; font-weight: 600; font-size: 10px; line-height: 12px; }
  .recipient-details { margin-top: 9px; }
  .salutation { margin-top: 13px; font-family: "Montserrat", sans-serif; font-weight: 600; font-size: 10px; }
  .letter-body p { text-align: justify; margin-bottom: 5px; }
  .letter-body p.last { text-align: left; }

  .sender { position: absolute; left: 57px; top: 446px; font-size: 11px; line-height: 13px; }
  .signature-line { margin-top: 28px; width: 81px; border-top: 1px solid var(--ink-soft); }
  .signature-label { margin-top: 1px; }

  .contact-list { position: absolute; right: 56px; top: 464px; list-style: none; font-size: 8.5px; letter-spacing: 0.06em; line-height: 14px; text-align: right; }
  .contact-list li { position: relative; padding-right: 18px; margin-bottom: 2px; }
  .contact-list li + li { margin-top: 4px; }
  .contact-list svg { position: absolute; right: 0; top: 2px; width: 10px; height: 10px; }

  /* compliment card */
  .card { left: 118px; top: 827px; width: 421px; height: 190px; }
  .card .brand { top: 86px; font-size: 14px; gap: 8px; }
  .card .brand-dot { width: 13px; height: 13px; }

  /* envelope back */
  .envelope { left: 669px; top: 827px; width: 421px; height: 190px; overflow: hidden; }
  .envelope-flap { position: absolute; left: 0; top: 0; width: 421px; height: 66px; }
  .envelope .brand { top: 80px; font-size: 11px; gap: 6px; }
  .envelope .brand-dot { width: 10px; height: 10px; }
</style>
</head>
<body>

  <section class="sheet cover">
    <div class="brand"><span class="brand-dot"></span>HALVERN PROPERTY SOLUTIONS</div>
    <div class="cover-taglines">
      <p>-The Rental Leader</p>
      <p>-Halvern Property Solutions</p>
      <p>-Serving Boston’s Real Estate Needs for 25+ Years !</p>
    </div>
  </section>

  <section class="sheet letterhead">
    <div class="brand"><span class="brand-dot"></span>HALVERN PROPERTY SOLUTIONS</div>
    <div class="letterhead-rule"></div>

    <div class="letter">
      <p>To.</p>
      <p class="person">Recipient's Name</p>
      <p class="role">Title</p>
      <div class="recipient-details">
        <p>Company Name</p>
        <p>Your Address Here</p>
        <p>Your Phone Number</p>
      </div>
      <p class="salutation">Dear Sir</p>
      <div class="letter-body">
        <p>There are many variations of passages of Lorem Ipsum available, but the majority have suffered alteration in some form, by injected humour, or randomised words which don't look even slightly believable. If you are going to use a passage of Lorem Ipsum, you need to be sure there isn't anything embarrassing hidden in the middle of text.</p>
        <p>All the Lorem Ipsum generators on the Internet tend to repeat predefined chunks as necessary, making this the first true generator on the Internet. It uses a dictionary of over 200 Latin words, combined with a handful of model sentence structures, to generate Lorem Ipsum which looks reasonable.</p>
        <p class="last">The generated Lorem Ipsum is therefore always free from repetition, injected humour, or non-characteristic words etc</p>
      </div>
    </div>

    <div class="sender">
      <p>From.</p>
      <p class="person">Your Name</p>
      <p class="role">Your Title</p>
      <div class="signature-line"></div>
      <p class="signature-label">Signature</p>
    </div>

    <ul class="contact-list">
      <li>Halvernpropertysolutions.com
        <svg viewBox="0 0 10 10" aria-hidden="true"><circle cx="5" cy="5" r="5" fill="#2b2b2b"/><g fill="none" stroke="#f5f5f5" stroke-width="0.7"><circle cx="5" cy="5" r="3.2"/><ellipse cx="5" cy="5" rx="1.4" ry="3.2"/><line x1="1.8" y1="5" x2="8.2" y2="5"/></g></svg>
      </li>
      <li>617-555-0148<br>617-555-0192
        <svg viewBox="0 0 10 10" aria-hidden="true"><circle cx="5" cy="5" r="5" fill="#2b2b2b"/><path d="M3.2 2.6l1 .1.5 1.3-.6.5c.3.7.8 1.2 1.5 1.5l.5-.6 1.3.5.1 1c-.2.4-.6.6-1 .5C4.6 7 3 5.4 2.6 3.6c-.1-.4.2-.8.6-1z" fill="#f5f5f5"/></svg>
      </li>
      <li>418 Linden Avenue,<br>Suite 2, Brighton, MA 02135
        <svg viewBox="0 0 10 10" aria-hidden="true"><circle cx="5" cy="5" r="5" fill="#2b2b2b"/><path d="M5 2.1a2 2 0 0 1 2 2c0 1.5-2 3.8-2 3.8S3 5.6 3 4.1a2 2 0 0 1 2-2z" fill="#f5f5f5"/><circle cx="5" cy="4.1" r="0.7" fill="#2b2b2b"/></svg>
      </li>
    </ul>
  </section>

  <section class="card">
    <div class="brand"><span class="brand-dot"></span>HALVERN PROPERTY SOLUTIONS</div>
  </section>

  <section class="envelope">
    <svg class="envelope-flap" viewBox="0 0 421 66" aria-hidden="true">
      <path d="M0 0 L421 0 L408 56 Q406 64 398 64 L23 64 Q15 64 13 56 Z" fill="#f5f5f5" stroke="#bdbdbd" stroke-width="1.2"/>
    </svg>
    <div class="brand"><span class="brand-dot"></span>HALVERN PROPERTY SOLUTIONS</div>
  </section>

</body>
</html>
```